National Australian HR & Recruitment Company

we need a document design (letter head / footer) for a proposal document to send to clients. This needs to include a design for the front page and some kind of water mark or design throughout the document.
The document needs to remain workable (word.doc) not PDF
The design should be elegant and corporate looking
The document is attached

Target Market(s)

Human Resource Managers. Corporate Clients

Industry/Entity Type

It Company

Font styles to use
Sans Serif

Requirements
Must have
• Must have a sleek elegant look

```html
<!DOCTYPE html>
<html lang="en">
<head>
<meta charset="utf-8">
<title>Authority for Service</title>
<link href="https://fonts.googleapis.com/css2?family=Arimo:ital,wght@0,400;0,700;1,400&display=swap" rel="stylesheet">
<style>
:root{
  --teal-dark:#4c877d;
  --teal-light:#5ea79b;
  --ink:#111;
  --title-grey:#555;
  --accent:#5a9c90;
  --rule:#333;
}
*{margin:0;padding:0;box-sizing:border-box}
html,body{width:848px;height:1200px;overflow:hidden;background:#fff}
body{font-family:"Arimo",Arial,sans-serif;color:var(--ink);position:relative;font-size:14.6px;line-height:1.3}
.side-band{position:absolute;left:0;top:0;width:34px;height:1200px;background:linear-gradient(180deg,var(--teal-dark) 0%,var(--teal-light) 30%,var(--teal-light) 70%,var(--teal-dark) 100%)}
.page-title{position:absolute;top:60px;left:0;width:896px;text-align:center;font-size:23px;font-weight:700;color:var(--title-grey);letter-spacing:.3px}
.abs{position:absolute}
.blank{display:inline-block;border-bottom:1px solid var(--rule);height:12px;vertical-align:baseline}
.justify{text-align:justify}
.section-head{position:absolute;left:89px;color:var(--accent);font-weight:700;font-size:14.6px}
.schedule p{margin-bottom:6px}
.details{position:absolute;left:86px;top:750px;width:685px;border-collapse:collapse}
.details th{background:var(--teal-dark);color:#fff;text-align:left;font-size:17.5px;font-weight:400;padding:0 14px;width:164px;height:34px;border-bottom:1px solid #3d6f66}
.details th.strong{font-weight:700}
.details td{border:1px solid #555;border-left:none;height:34px}
.details tr.tall th,.details tr.tall td{height:43px}
.footer-rule{position:absolute;left:145px;top:1136px;width:582px;height:2px;background:var(--teal-light)}
.footer-band{position:absolute;left:214px;top:1137px;width:436px;height:24px;background:var(--teal-light);border-radius:0 0 12px 12px}
.footer-text{position:absolute;top:1141px;left:257px;color:#fff;font-style:italic;font-size:12.8px;display:flex;gap:28px}
.footer-text a{color:#fff}
</style>
</head>
<body>

<div class="side-band" role="img" aria-label="Decorative teal side band"></div>

<h1 class="page-title">AUTHORITY FOR SERVICE</h1>

<p class="abs" style="top:123px;left:89px">Please complete and return the following Authority for Service to Miriam Castell, General Manager.</p>

<p class="abs" style="top:178px;left:89px;width:722px;display:flex;justify-content:space-between;align-items:baseline">
  <span>I,</span><span class="blank" style="width:176px"></span><span>holding the position of</span><span class="blank" style="width:176px"></span><span>with <b>Norvale Electrics</b></span>
</p>
<p class="abs" style="top:204px;left:89px">agree:</p>

<p class="abs justify" style="top:236px;left:141px;width:670px;line-height:24px"><span style="display:inline-block;width:52px">1.</span>To engage Brightpath Talent Partners in the provision of Outplacement Services as outlined in this Proposal ET4124 dated 26/09/2016, and</p>
<p class="abs" style="top:296px;left:141px"><span style="display:inline-block;width:52px">2.</span>To accept their fees and payment timeline as set out in the same document.</p>

<p class="abs" style="top:329px;left:93px">Purchase Order number &nbsp;<span class="blank" style="width:152px"></span> or &nbsp;Not Applicable</p>
<p class="abs" style="top:372px;left:93px">Signed: &nbsp;<span class="blank" style="width:334px"></span><span style="display:inline-block;width:18px"></span>Date: &nbsp;&nbsp;&nbsp;<span class="blank" style="width:128px"></span></p>

<h2 class="section-head" style="top:466px">Payment Schedule</h2>
<div class="abs schedule" style="top:492px;left:89px;width:722px">
  <p class="justify" style="line-height:17px">You shall be invoiced upon signed authority of service or individual commencement of the outplacement program, as appropriate.</p>
  <p>Full payment is required within 7 days from date of invoice.</p>
  <p>Quoted fees are subject to GST.</p>
  <p>Fees include all individual resources &amp; materials unless stated otherwise.</p>
  <p style="line-height:17px">Disbursements such as travel and accommodation will be invoiced at cost should consultations be required outside of the metro city area.</p>
</div>

<h2 class="section-head" style="top:703px">Company details</h2>
<table class="details">
  <tr><th class="strong">Contact:</th><td></td></tr>
  <tr><th>Position:</th><td></td></tr>
  <tr><th>Phone:</th><td></td></tr>
  <tr><th>Email:</th><td></td></tr>
  <tr><th class="strong">Company Name:</th><td></td></tr>
  <tr class="tall"><th>ABN:</th><td></td></tr>
</table>

<div class="footer-rule"></div>
<div class="footer-band"></div>
<div class="footer-text">
  <span>1300 555 019</span>
  <a href="#">www.brightpathtalent.com.au</a>
  <span>Page 6</span>
</div>

</body>
</html>
```